Keystone Prime Water Tank

I primarily market the water tanks so want a business care that reflects that. I have attached the water tank logo. You have been working on our water tank so maybe we can use that on the card et. I am leaving as one sided but can be double sided if that works. The information that needs to be on the cards is as follows: Gerald T. Munro Phone numbers: Office 555-284-9137 Direct 555-619-2405 Mobile 555-372-5841 email address: gerald@fieldgearworks.com Address P.O. Box 8273 Cedar Hollow, OH 30512 Web Page: www.fieldgearworks.com. A lot to fit on the card. Thanks

```html
<!DOCTYPE html>
<html lang="en">
<head>
<meta charset="utf-8">
<title>Keystone Prime Water Tank – Business Card</title>
<link rel="stylesheet" href="https://fonts.googleapis.com/css2?family=Oswald:wght@500;600;700&display=swap">
<style>
  :root {
    --canvas-bg: #c9c9c9;
    --card-white: #ffffff;
    --brand-red: #ff0000;
    --ink: #111111;
    --text-light: #ffffff;
    --sky: #8fb6e0;
    --machine: #e8b21c;
    --ground: #6e5a3e;
  }
  * { margin: 0; padding: 0; box-sizing: border-box; }
  html, body {
    width: 1200px; height: 1200px; overflow: hidden;
    background: var(--canvas-bg);
    font-family: "Oswald", sans-serif;
  }
  .sheet {
    width: 1200px; height: 1200px;
    display: flex; flex-direction: column; align-items: center; justify-content: space-evenly;
  }
  .card {
    width: 840px; height: 480px;
    box-shadow: 0 6px 18px rgba(0,0,0,0.15);
  }
  .card svg { display: block; width: 100%; height: 100%; }
  .card--front {
    background: var(--card-white);
    display: flex; align-items: center; justify-content: center; gap: 18px;
  }
  .brand-mark { width: 34px; height: 34px; background: var(--brand-red); }
  .brand-name {
    color: var(--ink); font-weight: 700; font-size: 34px;
    letter-spacing: 1px; text-transform: uppercase; line-height: 1;
  }
  .contact-name { font-weight: 700; fill: var(--text-light); }
  .contact-line { font-weight: 500; fill: var(--text-light); }
  .web-address { font-weight: 600; fill: var(--text-light); }
  .badge-name { font-weight: 700; fill: var(--ink); }
</style>
</head>
<body>
<main class="sheet">

  <section class="card card--front" aria-label="Card front">
    <span class="brand-mark"></span>
    <span class="brand-name">Keystone Prime Water Tank</span>
  </section>

  <section class="card card--back" aria-label="Card back">
    <svg viewBox="0 0 403 230" xmlns="http://www.w3.org/2000/svg">
      <defs>
        <linearGradient id="photoTone" x1="0" y1="0" x2="0" y2="1">
          <stop offset="0" stop-color="var(--sky)"/>
          <stop offset="0.45" stop-color="var(--machine)"/>
          <stop offset="1" stop-color="var(--ground)"/>
        </linearGradient>
      </defs>
      <rect class="card-bg" width="403" height="230" fill="var(--brand-red)"/>

      <text class="contact-name" x="14" y="37" font-size="17">GERALD T. MUNRO</text>

      <g class="contact-list" font-size="7.5">
        <text class="contact-line" x="27" y="55">Office 555-284-9137</text>
        <g class="icon-phone" fill="var(--text-light)">
          <path d="M13.5 65.5 q1-1 2 0 l1 1.5 q.4.8-.4 1.3 q.8 1.8 2.6 2.6 q.5-.8 1.3-.4 l1.5 1 q1 1 0 2 q-1.5 1.5-4-.2 q-3.5-2.5-4.6-5 q-.9-1.9.6-2.8z"/>
        </g>
        <text class="contact-line" x="27" y="72">Direct 555-619-2405</text>
        <text class="contact-line" x="27" y="89">Mobile 555-372-5841</text>
        <g class="icon-mail">
          <rect x="13" y="100.5" width="9" height="6.5" fill="var(--text-light)"/>
          <path d="M13 100.5 l4.5 3.6 l4.5-3.6" fill="none" stroke="var(--brand-red)" stroke-width=".8"/>
        </g>
        <text class="contact-line" x="27" y="106">gerald@fieldgearworks.com</text>
        <g class="icon-pin" fill="var(--text-light)">
          <path d="M17.5 116 a3.5 3.5 0 0 1 3.5 3.5 q0 2.4-3.5 6 q-3.5-3.6-3.5-6 a3.5 3.5 0 0 1 3.5-3.5z"/>
          <circle cx="17.5" cy="119.5" r="1.3" fill="var(--brand-red)"/>
        </g>
        <text class="contact-line" x="27" y="123">P.O. Box 8273 Cedar Hollow, OH 30512</text>
      </g>

      <polygon class="machine-photo" role="img"
        aria-label="Photo of a yellow articulated water tank truck on a dirt site under blue sky"
        points="248,1 88,230 392,230" fill="url(#photoTone)" stroke="var(--card-white)" stroke-width="3"/>

      <g class="name-badge">
        <polygon points="75,138 25,230 125,230" fill="var(--card-white)"/>
        <rect x="69" y="182" width="12" height="12" fill="var(--brand-red)"/>
        <text class="badge-name" x="75" y="207" font-size="7.5" text-anchor="middle">KEYSTONE PRIME</text>
        <text class="badge-name" x="75" y="216" font-size="7.5" text-anchor="middle">WATER TANK</text>
      </g>

      <text class="web-address" font-size="9.5" transform="translate(288 38) rotate(55)">www.fieldgearworks.com</text>
    </svg>
  </section>

</main>
</body>
</html>
```